Tufted Hollow is company name.Handknit&crochet blankets&scarves. Need logo&business ...

I need a design that is eye catching, using yarn and is flowing. I'd like to see colors in aqua (Larkin Peabody paint LP9043 Aquastone) for the yarn and company name. For the text, a dark grey color (Larkin Peabody LP7622 Hamburg Gray)

Colors
87cfc7

```html
<!DOCTYPE html>
<html lang="en">
<head>
<meta charset="utf-8">
<title>Tufted Hollow — Business Card</title>
<link rel="stylesheet" href="https://fonts.googleapis.com/css2?family=Oswald:wght@300&display=swap">
<style>
  :root {
    --page: #ffffff;
    --card: #e0eeeb;
    --aqua: #87cfc7;
    --rule: #7fcfc4;
    --ink: #7a7d7c;
  }
  html, body {
    margin: 0;
    padding: 0;
    width: 1200px;
    height: 1200px;
    overflow: hidden;
    background: var(--page);
  }
  .canvas {
    position: relative;
    width: 1200px;
    height: 1200px;
  }
  .card {
    position: absolute;
    left: 36px;
    top: 312px;
    width: 1128px;
    height: 624px;
    background: var(--card);
  }
  .card-frame {
    position: absolute;
    left: 26px;
    top: 29px;
    right: 24px;
    bottom: 26px;
    border: 2px solid var(--rule);
  }
  .brand-name {
    position: absolute;
    left: 100px;
    top: 95px;
    margin: 0;
    font-family: "Oswald", sans-serif;
    font-weight: 300;
    font-size: 104px;
    line-height: 1;
    color: var(--aqua);
    letter-spacing: 1px;
  }
  .info {
    position: absolute;
    top: 350px;
    margin: 0;
    padding: 0;
    list-style: none;
    font-family: "Oswald", sans-serif;
    font-weight: 300;
    font-size: 34px;
    line-height: 55px;
    color: var(--ink);
    text-transform: uppercase;
    letter-spacing: 0.3px;
  }
  .contact { left: 100px; }
  .offerings { left: 686px; }
</style>
</head>
<body>
  <div class="canvas">
    <section class="card">
      <div class="card-frame"></div>
      <h1 class="brand-name">Tufted Hollow</h1>
      <ul class="info contact">
        <li>Dana Whitlock</li>
        <li>Phone#</li>
        <li>Email Adress</li>
      </ul>
      <ul class="info offerings">
        <li>Hand Knit: Crochet</li>
        <li>Baby Afghans</li>
        <li>Afghans</li>
        <li>Scarves, Gloves, Hats</li>
      </ul>
    </section>
  </div>
</body>
</html>
```